Company Website

Our company teaches Corvane Accredited Medic certification. Our company name is Harbrook Training Group. (logo is in the files). We have a current website that needs an overhaul (www.harbrooktraininggroup.com). This website needs to able to be used on wordpress. We need a website that has a good flow and design, have a page that has our instructor bio’s, a page on our class information, prerequisites, and how many seats are left in the class, a page that will accept payments and layout our cost. Be able to expand as our company expands to other classes (CPR ETC.)

Target Market(s)

People that want to take an EMT class

Coding

Coded - Design and coding required

Number of Pages Required

3 page

Requirements
Must have
• A page explaining who we are, a page of the services we offer with the ability to pay using Quidlo or some external source, and a page about who the instructors are.
Nice to have
• Good flow, easy to change as the Business grows

```html
<!DOCTYPE html>
<html lang="en">
<head>
<meta charset="utf-8">
<title>Harbrook Training Group</title>
<link rel="stylesheet" href="https://fonts.googleapis.com/css2?family=Rubik:wght@400;500;700&family=Catamaran:wght@500;600&display=swap">
<style>
:root{
  --ink:#222;
  --navy:#2b3640;
  --navy-deep:#1f2830;
  --red:#d9252d;
  --red-dark:#a8161c;
  --grey-band:#ececec;
  --grey-soft:#f5f5f5;
  --teal:#2fb59e;
  --line:#c9c9c9;
  --white:#fff;
  --muted:#555;
}
*{box-sizing:border-box;margin:0;padding:0}
html,body{width:1200px;height:4412px;overflow:hidden}
body{position:relative;font-family:"Rubik",sans-serif;color:var(--ink);background:var(--white)}
.abs{position:absolute}
.pill{position:absolute;display:flex;align-items:center;justify-content:center;border-radius:30px;font-family:"Rubik",sans-serif}
.red-pill{background:var(--red);color:var(--white)}
.section-title{position:absolute;left:0;width:1200px;text-align:center;font-family:"Catamaran",sans-serif;font-weight:600;font-size:44px;color:var(--ink)}

/* header */
.site-header{position:absolute;left:0;top:0;width:1200px;height:90px;background:var(--navy);z-index:3}
.brand{position:absolute;display:flex;align-items:center;gap:10px;font-family:"Rubik",sans-serif;font-weight:500;color:var(--red)}
.brand-dot{border-radius:50%;background:var(--red)}
.main-nav a{position:absolute;top:36px;color:#d8dde2;font-size:16px;text-decoration:none}

/* hero */
.hero{position:absolute;left:0;top:90px;width:1200px;height:700px;overflow:hidden}
.hero-photo{position:absolute;inset:0;background:radial-gradient(ellipse at 75% 45%,#c0262a 0%,#6d1518 35%,#2a1214 65%,#131416 100%)}
.hero h1{position:absolute;left:153px;top:170px;font-size:62px;line-height:66px;color:var(--white);font-weight:400;letter-spacing:-1px}
.hero h1 b{font-weight:700}
.hero p{position:absolute;left:153px;top:335px;font-size:20px;color:var(--white)}

/* welcome */
.welcome-art{position:absolute;left:85px;top:875px;width:425px;height:300px;border-radius:20px;background:radial-gradient(ellipse at center,#c4454a 0%,#7a2f4c 45%,#ffffff 75%)}
.welcome h2{position:absolute;left:565px;top:890px;font-size:34px;line-height:40px;font-weight:700;letter-spacing:-.5px}
.welcome p{position:absolute;left:565px;top:1003px;width:500px;font-size:12.5px;line-height:24px;color:#333}

/* services */
.services{position:absolute;left:0;top:1315px;width:1200px;height:750px;background:var(--grey-band)}
.service-card{position:absolute;top:1543px;width:312px;height:254px;background:#f7f7f7;border:1px solid #d6d6d6;box-shadow:0 2px 6px rgba(0,0,0,.15);text-align:center}
.service-card h3{margin-top:72px;font-size:16px;font-weight:400;color:var(--red)}
.service-card p{margin:10px auto 0;width:240px;font-size:13px;line-height:19px;color:#444}
.service-card .outline-btn{margin:14px auto 0;width:150px;height:38px;border:2px solid #666;border-radius:20px;font-size:14px;color:#444;display:flex;align-items:center;justify-content:center}
.service-icon{position:absolute;top:1500px;width:92px;height:92px;border-radius:50%;background:var(--red);display:flex;align-items:center;justify-content:center}
.query{position:absolute;left:160px;top:1862px;font-family:"Catamaran",sans-serif;font-size:29px;line-height:44px;color:#333}
.query .phone{color:var(--teal);font-size:33px;letter-spacing:1px}

/* mission (children positioned relative to section) */
.mission{position:absolute;left:0;top:2065px;width:1200px;height:655px;overflow:hidden}
.mission-title{position:absolute;left:608px;top:243px;width:470px;font-size:20px;line-height:30px;font-weight:700;color:var(--white)}
.mission-rule{position:absolute;left:610px;top:345px;width:95px;height:2px;background:var(--white)}
.mission-text{position:absolute;left:608px;top:370px;width:460px;font-size:12.5px;line-height:24px;color:var(--white)}

/* seats */
.seats{position:absolute;left:0;top:2720px;width:1200px;height:205px;overflow:hidden}

/* testimonial */
.quote-card{position:absolute;left:365px;top:3135px;width:480px;height:222px;background:var(--white);box-shadow:0 6px 24px rgba(0,0,0,.12);text-align:center}
.quote-card p{position:absolute;left:110px;top:66px;width:280px;font-size:14px;line-height:24px;color:#444}
.quote-card .name{position:absolute;left:0;width:480px;top:170px;font-family:"Catamaran",sans-serif;font-size:22px;color:var(--red)}

/* contact */
.contact{position:absolute;left:0;top:3465px;width:1200px;height:540px;background:var(--grey-soft)}
.field{position:absolute;width:315px;height:48px;border:2px solid #ddd;background:var(--white);padding:12px 18px;font-size:17px;color:#666;font-family:"Rubik",sans-serif}

/* footer */
.site-footer{position:absolute;left:0;top:3985px;width:1200px;height:427px}
.footer-heading{position:absolute;top:4105px;font-size:16px;font-weight:500;color:#d8dde2;letter-spacing:.3px}
.footer-links{position:absolute;left:544px;top:4148px;list-style:none}
.footer-links li{font-size:14px;line-height:27px;color:#c5cbd1}
.social{position:absolute;top:4281px;width:32px;height:32px;border:1.5px solid #c5cbd1;border-radius:50%}
</style>
</head>
<body>

<header class="site-header">
  <div class="brand" style="left:55px;top:28px;font-size:22px">
    <span class="brand-dot" style="width:22px;height:22px"></span>Harbrook Training Group
  </div>
  <nav class="main-nav">
    <a style="left:555px">HOME</a>
    <a style="left:642px">ABOUT</a>
    <a style="left:737px">EMT CLASS</a>
    <a style="left:866px">BLOG</a>
  </nav>
  <div class="pill" style="left:943px;top:23px;width:194px;height:45px;background:#5b6772;color:var(--white);font-size:16px">CONTACT WITH US</div>
</header>

<section class="hero">
  <div class="hero-photo" role="img" aria-label="Ambulance speeding through the night with motion blur"></div>
  <h1><b>Emergency</b> Medical<br>Technicians</h1>
  <p>Here at Harbrook Training Group we care about your success.</p>
  <div class="pill red-pill" style="left:153px;top:412px;width:252px;height:52px;font-size:17px;font-weight:500">Explore Our EMT Class</div>
  <svg class="abs" style="left:0;top:0" width="1200" height="700" viewBox="0 0 1200 700">
    <path d="M0 590 Q600 830 1200 590 L1200 700 L0 700 Z" fill="#5d6670"/>
    <path d="M0 602 Q600 818 1200 602 L1200 700 L0 700 Z" fill="#fff"/>
    <circle cx="578" cy="595" r="6" fill="#fff"/>
    <circle cx="600" cy="595" r="8" fill="#fff"/>
    <circle cx="623" cy="595" r="6" fill="#fff"/>
  </svg>
</section>

<section class="welcome">
  <div class="welcome-art" role="img" aria-label="Decorative medical training emblem artwork"></div>
  <h2>WELCOME TO<br>HARBROOK TRAINING GROUP</h2>
  <div class="abs" style="left:567px;top:985px;width:100px;height:3px;background:var(--red)"></div>
  <p>Emergency Medical Technicians or EMTs provide basic emergency medical care and transportation for critical and emergent patients who access the emergency medical system. This individual possess the basic knowledge and skills necessary to provide patient care and transportation. Emergency Medical Technicians function as part of a comprehensive EMS response.</p>
  <div class="pill red-pill" style="left:567px;top:1163px;width:172px;height:46px;font-size:17px;font-weight:500">Learn More</div>
</section>

<section class="services">
  <h2 class="section-title" style="top:88px">Services Offered?</h2>
</section>
<article class="service-card" style="left:106px"><h3>HARBROOK TRAINING GROUP</h3><p>Lorem Ipsum is simply dummy text of the printing and typesetting industry. Lorem Ipsum has been</p><div class="outline-btn">LEARN MORE</div></article>
<article class="service-card" style="left:444px"><h3>HIGH QUALITY TRAINING</h3><p>Lorem Ipsum is simply dummy text of the printing and typesetting industry. Lorem Ipsum has been</p><div class="outline-btn">LEARN MORE</div></article>
<article class="service-card" style="left:782px"><h3>JOINING OUR CLASS</h3><p>Lorem Ipsum is simply dummy text of the printing and typesetting industry. Lorem Ipsum has been</p><div class="outline-btn">LEARN MORE</div></article>
<div class="service-icon" style="left:216px"><svg width="46" height="46" viewBox="0 0 46 46" fill="none" stroke="#fff" stroke-width="2.5"><circle cx="25" cy="16" r="9"/><path d="M25 11v10M4 34h10l8 4 16-8"/></svg></div>
<div class="service-icon" style="left:554px"><svg width="40" height="46" viewBox="0 0 40 46" fill="none" stroke="#fff" stroke-width="2.5"><rect x="6" y="4" width="28" height="38" rx="2"/><path d="M12 14h16M12 21h16M12 28h16M12 35h10"/></svg></div>
<div class="service-icon" style="left:892px"><svg width="46" height="46" viewBox="0 0 46 46" fill="none" stroke="#fff" stroke-width="2.5"><circle cx="23" cy="23" r="16"/><path d="M12 26l7-5 8 6 7-5"/></svg></div>
<div class="query">If you want to know more, submit a query<br>or call <span class="phone">555 0142 736</span></div>
<div class="pill red-pill" style="left:847px;top:1878px;width:209px;height:52px;font-family:'Catamaran',sans-serif;font-size:24px;font-weight:500">Sent Request</div>

<section class="mission">
  <div class="abs" role="img" aria-label="Ambulance parked in a dim tunnel" style="inset:0;background:radial-gradient(ellipse at 55% 50%,#3c3f44 0%,#26292d 60%,#1b1d20 100%)"></div>
  <svg class="abs" style="left:0;top:0" width="1200" height="655" viewBox="0 0 1200 655">
    <path d="M0 0 L1200 0 L1200 125 Q600 -50 0 125 Z" fill="#ececec"/>
    <path d="M0 118 Q600 -52 1200 118" fill="none" stroke="#9a9a9a" stroke-width="3"/>
  </svg>
  <div class="abs" role="img" aria-label="Police car and ambulance lights at an emergency scene" style="left:142px;top:150px;width:420px;height:420px;border-radius:50%;background:radial-gradient(circle at 40% 55%,#7d8da0 0%,#3b4554 45%,#16191e 100%)"></div>
  <svg class="abs" style="left:130px;top:140px" width="440" height="440" viewBox="0 0 440 440"><path d="M220 10 A210 210 0 0 1 220 430" fill="none" stroke="var(--red)" stroke-width="4"/></svg>
  <h2 class="mission-title">WE TEACH CORVANE ACCREDITED MEDIC, CPR, AND CONTINUING EDUCATION CLASSES FOR BOTH ALS AND BLS PROVIDERS.</h2>
  <div class="mission-rule"></div>
  <p class="mission-text">Our passion is to give high quality training to those that help others. Here at Harbrook Training Group we care about your success. Let us help you in the many different training opportunities available.</p>
</section>

<section class="seats">
  <div class="abs" role="img" aria-label="Row of ambulances in red tone" style="inset:0;background:linear-gradient(90deg,#8d1a1f,#b42a2f 60%,#7a1519)"></div>
  <svg class="abs" style="left:0;top:0" width="1200" height="205" viewBox="0 0 1200 205"><path d="M0 0 L540 0 L633 205 L0 205 Z" fill="var(--red)"/></svg>
  <div class="abs" style="left:140px;top:45px;width:400px;text-align:center;font-size:43px;font-weight:500;color:#fff">15 Seats Left!!</div>
  <div class="pill" style="left:219px;top:120px;width:252px;height:40px;background:#fff;color:var(--red);font-size:17px">Explore Our EMT Class</div>
  <div class="abs" style="left:650px;top:63px;width:416px;text-align:center;font-size:19px;font-weight:500;color:#fff">February-2021-EMT-Schedule-1</div>
  <div class="pill" style="left:782px;top:118px;width:171px;height:37px;background:#fff;color:var(--red);font-size:15px">Download Now</div>
</section>

<section class="testimonial">
  <h2 class="section-title" style="top:3005px;left:320px;width:600px">Testimonial</h2>
  <div class="abs" style="left:560px;top:3068px;width:120px;height:3px;background:var(--red)"></div>
  <div class="quote-card">
    <svg class="abs" style="left:233px;top:-4px" width="52" height="44" viewBox="0 0 52 44" fill="none" stroke="var(--red)" stroke-width="2.5"><path d="M4 42V22C4 10 10 4 20 2M8 22h14v20H4M28 42V22c0-12 6-18 16-20M32 22h14v20H28"/></svg>
    <p>Lorem ipsum dolor sit amet, consectetur adipiscing elit, sed do eiusmod tempor incididunt ut labore et dolore magna dolore aliqua.</p>
    <div class="name">Mara Telford</div>
  </div>
  <div class="abs" role="img" aria-label="Portrait of the reviewer" style="left:262px;top:3080px;width:162px;height:162px;border-radius:50%;background:radial-gradient(circle,#c9a38a 0%,#8a9aa8 100%)"></div>
  <div class="abs" style="left:797px;top:3318px;width:48px;height:48px;background:#fff;box-shadow:0 2px 8px rgba(0,0,0,.15);display:flex;align-items:center;justify-content:center"><svg width="12" height="14" viewBox="0 0 12 14"><path d="M9 2L3 7l6 5" fill="none" stroke="#222" stroke-width="2.5"/></svg></div>
  <div class="abs" style="left:845px;top:3318px;width:48px;height:48px;background:var(--red);display:flex;align-items:center;justify-content:center"><svg width="12" height="14" viewBox="0 0 12 14"><path d="M3 2l6 5-6 5" fill="none" stroke="#fff" stroke-width="2.5"/></svg></div>
</section>

<section class="contact">
  <h2 class="section-title" style="top:72px">Get In Touch</h2>
</section>
<div class="field" style="left:273px;top:3618px">Your Name</div>
<div class="field" style="left:612px;top:3618px">Subject</div>
<div class="field" style="left:273px;top:3690px">Email Address</div>
<div class="field" style="left:612px;top:3690px;height:120px"></div>
<div class="field" style="left:273px;top:3762px">Phone</div>
<div class="pill red-pill" style="left:517px;top:3845px;width:167px;height:48px;font-size:16px;font-weight:500">LEARN MORE</div>

<footer class="site-footer">
  <svg class="abs" style="left:0;top:0" width="1200" height="427" viewBox="0 0 1200 427">
    <rect width="1200" height="427" fill="var(--navy-deep)"/>
    <path d="M0 0 L1200 0 L1200 95 Q600 -60 0 95 Z" fill="var(--grey-soft)"/>
    <path d="M0 95 Q600 -60 1200 95 L1200 110 Q600 -20 0 110 Z" fill="#3c4650"/>
  </svg>
</footer>
<div class="brand" style="left:132px;top:4132px;font-size:26px">
  <span class="brand-dot" style="width:26px;height:26px"></span>Harbrook Training Group
</div>
<div class="abs" style="left:132px;top:4236px;font-size:13px;color:#c5cbd1">© 2020 Pellwick Studio. All Rights are Reserved.</div>
<span class="social" style="left:136px" aria-label="Social link"></span>
<span class="social" style="left:176px" aria-label="Social link"></span>
<span class="social" style="left:215px" aria-label="Social link"></span>
<span class="social" style="left:254px" aria-label="Social link"></span>
<div class="footer-heading" style="left:544px">QUICK LINKS</div>
<ul class="footer-links"><li>Home</li><li>About Us</li><li>EMT Class</li><li>Blog</li><li>Tearm</li><li>How its works</li><li>Contact Us</li></ul>
<div class="footer-heading" style="left:725px">SIGN UP FOR NEWSLETTER</div>
<div class="abs" style="left:725px;top:4150px;width:370px;font-size:14px;line-height:22px;color:#c5cbd1">If you are interested in joining our class, or have any questions please send us a message.</div>
<div class="abs" style="left:725px;top:4218px;width:310px;height:44px;border:1.5px solid #8a949d;border-radius:22px;overflow:hidden;display:flex">
  <span style="flex:1;padding:12px 26px;font-size:14px;color:#9aa3ab">Email address</span>
  <span style="width:114px;background:#5b6772;color:#fff;font-size:15px;display:flex;align-items:center;justify-content:center">Subscribe</span>
</div>
<div class="pill red-pill" style="left:725px;top:4295px;width:308px;height:43px;font-size:13.5px">SCHEDULE FREE 15 MIN CONSULTATION</div>

</body>
</html>
```